Cedarline Coalition Web Presence Design and Relaunch

Take existing web files and "clean up" for a a more presentable web landing pad.
posted presently on a site pad CSS template. at www.cedarlinecoalition.org

The site is clunky and unprofessional looking. Needs to be toned down so the urgency is conveyed, but not via a burning planet image.

Target Market(s)

Non-profit climate adaptation group targeting local government land management agencies, special districts and private landholders of natural resource properties.

Industry/Entity Type

Environment

Coding

Coded - Design and coding required

Number of Pages Required

Font styles to use
Serif
Sans Serif

Requirements
Must have
• Include current logos, aspects if content on current site www.cedarlinecoalition.org
• A regional Pacific Northwest Focus (US & Canada). Content speaking to urgency but respectful of cultural diversity and norms. Sustainability themes. Emphasis on action and implementation.
Nice to have
• link to like minded projects. Appear to future generations. Diversity in thematic areas ecological resiliency, energy, food security and infrastructure.

```html
<!DOCTYPE html>
<html lang="en">
<head>
<meta charset="utf-8">
<title>Cedarline Coalition — Implementing Climate Adaptation</title>
<link rel="stylesheet" href="https://fonts.googleapis.com/css2?family=Playfair+Display:wght@400;700;900&family=Poppins:wght@300;400;500;600&display=swap">
<style>
:root{
  --wine:#7a0c16;
  --wine-dark:#5e0810;
  --bronze:#8d6a3f;
  --ink:#222222;
  --muted:#666666;
  --paper:#ffffff;
  --mist:#e7e7e7;
  --navy:#1f2231;
  --navy-deep:#181a26;
  --card-line:#d9d9d9;
}
*{box-sizing:border-box;margin:0;padding:0}
html,body{width:1200px;height:3644px;overflow:hidden}
body{font-family:"Poppins",sans-serif;color:var(--ink);background:var(--paper);position:relative}

/* Header + hero */
.hero{position:relative;height:580px;background:radial-gradient(ellipse at 50% 20%,#5a4a3c 0%,#2e2722 45%,#171311 100%);overflow:hidden}
.hero-photo{position:absolute;inset:0;background:radial-gradient(circle at 50% 30%,rgba(230,150,80,.35) 0,rgba(120,70,40,.15) 25%,transparent 45%),radial-gradient(ellipse at 50% 92%,rgba(190,110,80,.45) 0,transparent 45%)}
.site-nav{position:absolute;top:0;left:0;right:0;height:56px;display:flex;align-items:center;justify-content:space-between;padding:0 90px;z-index:2}
.brand{font-weight:600;font-size:15px;color:#fff;display:flex;align-items:center;gap:8px}
.brand-dot{width:14px;height:14px;border-radius:50%;background:#fff}
.nav-links{display:flex;gap:46px;list-style:none}
.nav-links li{font-size:12px;color:#fff;letter-spacing:.06em;font-weight:500}
.hero-copy{position:absolute;top:120px;left:0;right:0;text-align:center;color:#fff;z-index:2}
.hero-kicker{font-family:"Playfair Display",serif;font-size:26px;font-style:italic}
.hero-title{font-family:"Playfair Display",serif;font-size:48px;font-weight:700;margin-top:4px}
.hero-text{width:700px;margin:12px auto 0;font-size:14px;line-height:1.45;color:#eee}
.btn{display:inline-block;background:var(--wine);color:#fff;font-size:11px;font-weight:600;letter-spacing:.06em;padding:12px 26px;border-radius:22px}
.hero .btn{margin-top:22px}
.hero-marker{position:absolute;bottom:-12px;left:588px;width:24px;height:24px;border-radius:50%;background:#fff;border:1px solid #ccc;z-index:3}

/* Featured projects */
.projects{padding:60px 0 0;text-align:center;height:480px}
.section-title{font-family:"Playfair Display",serif;font-weight:700;font-size:46px;color:var(--ink)}
.title-rule{width:120px;height:2px;background:var(--bronze);margin:8px auto 0}
.project-grid{display:flex;gap:20px;justify-content:center;margin-top:28px}
.project-card{width:206px;height:318px;border:1px solid var(--card-line);padding:22px 14px;background:#fff;box-shadow:0 2px 6px rgba(0,0,0,.05);overflow:hidden}
.icon-ring{width:70px;height:70px;border-radius:50%;background:var(--bronze);margin:0 auto;display:flex;align-items:center;justify-content:center}
.project-card h3{font-size:14.5px;font-weight:600;margin-top:18px;white-space:nowrap}
.project-card p{font-size:11.5px;line-height:1.55;color:var(--muted);margin-top:10px}

/* What we are doing */
.doing{position:relative;height:640px}
.doing-panel{position:absolute;left:0;top:100px;width:700px;height:540px;background:var(--wine);color:#fff;padding:120px 70px 0 60px}
.doing-panel h2{font-family:"Playfair Display",serif;font-size:46px;font-weight:900;line-height:1.05}
.doing-panel p{font-size:13px;line-height:1.7;margin-top:22px;width:460px;color:#f3dcdc}
.doing-photo{position:absolute;right:0;top:4px;width:620px;height:540px;background:linear-gradient(135deg,#c8b49a 0%,#a88a6b 40%,#6f5a49 100%)}

/* Stats */
.stats{height:290px;background:linear-gradient(90deg,#2a2826,#3c3935 50%,#262422);display:flex;justify-content:center;gap:140px;align-items:center;color:#fff;text-align:center}
.stat-num{font-size:40px;font-weight:600;margin-top:12px}
.stat-label{font-size:13px;color:#ddd}

/* Themes */
.themes{display:flex;gap:22px;justify-content:center;margin-top:100px;height:252px}
.theme-card{width:240px;background:var(--mist)}
.theme-photo{height:196px}
.theme-card h4{font-size:15px;font-weight:500;text-align:center;margin-top:10px}
.theme-card span{display:block;font-size:10.5px;color:var(--muted);text-align:center;padding:4px 0 12px}

/* Save money */
.savings{display:flex;padding:0 92px;margin-top:150px;height:170px;align-items:center}
.savings-head{width:450px}
.savings-head .top{font-family:"Playfair Display",serif;font-size:40px;font-weight:700;color:var(--wine)}
.savings-head .big{font-family:"Playfair Display",serif;font-size:76px;font-weight:900;color:var(--wine);line-height:1}
.bars{flex:1}
.bar-row{margin-bottom:14px}
.bar-label{font-size:11px;font-weight:500;margin-bottom:4px}
.bar-track{position:relative;height:12px;background:#eee;border-radius:6px}
.bar-fill{height:12px;border-radius:6px}
.bar-val{position:absolute;right:-4px;top:-4px;font-size:10px;background:#fff;border:1px solid #ccc;border-radius:10px;padding:1px 6px}

/* Contact */
.contact{display:flex;height:496px;margin-top:68px}
.contact-info{width:520px;background:var(--mist);padding:80px 0 0 92px}
.contact-info h2{font-family:"Playfair Display",serif;font-size:42px;font-weight:700}
.info-line{display:flex;gap:10px;align-items:flex-start;font-size:12px;color:#444;margin-top:16px;line-height:1.4}
.follow{font-family:"Playfair Display",serif;font-size:24px;font-weight:700;margin-top:30px}
.social{display:flex;gap:8px;margin-top:10px}
.social i{width:28px;height:28px;background:var(--bronze);display:block}
.contact-form{flex:1;background:var(--wine);padding:70px 80px 0 46px;color:#fff}
.contact-form h2{font-family:"Playfair Display",serif;font-size:42px;font-weight:700}
.form-grid{display:grid;grid-template-columns:1fr 1fr;gap:12px 20px;margin-top:30px}
.field{height:32px;background:#fff;border-radius:16px;font-size:11px;color:#888;padding:8px 16px}
.field.area{grid-column:1/3;height:120px;border-radius:14px}
.contact-form .btn{margin-top:26px;background:var(--wine-dark);border:1px solid #fff}

/* Footer */
.footer{position:relative;height:420px;background:var(--navy);color:#fff}
.footer-cols{display:flex;padding:90px 92px 0}
.footer-brand{width:300px}
.footer-brand .name{font-size:24px;font-weight:600}
.footer-brand .tag{font-size:13px;color:#ccc;margin-top:10px}
.footer-social{display:flex;gap:10px;margin-top:22px}
.footer-social i{width:30px;height:30px;border-radius:50%;background:#fff;display:block}
.footer-col{width:250px}
.footer-col h5{font-size:15px;font-weight:600;margin-bottom:16px}
.footer-col li{list-style:none;font-size:12px;color:#ccc;margin-bottom:10px;display:flex;gap:8px;align-items:center}
.map{width:200px;height:130px;background:linear-gradient(135deg,#dfe6e0,#c9d6e3)}
.footer-bar{position:absolute;bottom:0;left:0;right:0;height:56px;background:var(--navy-deep);display:flex;align-items:center;justify-content:center;font-size:11px;color:#aaa;border-top:1px solid #333}
</style>
</head>
<body>

<header class="hero">
  <div class="hero-photo" role="img" aria-label="Open hands holding a glowing globe against a warm dark background"></div>
  <nav class="site-nav">
    <div class="brand"><span class="brand-dot"></span>Cedarline Coalition</div>
    <ul class="nav-links"><li>HOME</li><li>ABOUT</li><li>EVENTS</li><li>CONTACT</li></ul>
  </nav>
  <div class="hero-copy">
    <div class="hero-kicker">Climate Adaptation</div>
    <h1 class="hero-title">Implementing Climate Strategies</h1>
    <p class="hero-text">Dedicated to taking action that helps the Pacific Northwest adapt to a changing climate. Working with local communities we are committed to implementing strategies that will sustain our region for generations to come.</p>
    <span class="btn">CONTACT US</span>
  </div>
  <span class="hero-marker"></span>
</header>

<section class="projects">
  <h2 class="section-title">Featured Projects</h2>
  <div class="title-rule"></div>
  <div class="project-grid">
    <article class="project-card">
      <div class="icon-ring"><svg width="34" height="34" viewBox="0 0 24 24" fill="none" stroke="#fff" stroke-width="1.6"><rect x="5" y="3" width="14" height="18" rx="1"/><path d="M8 8h8M8 12h8M8 16h5"/></svg></div>
      <h3>Adaptation Plans</h3>
      <p>Communities throughout the region have adopted plans to address our changing climate. We now need to put these plans into action, working alongside each community to implement them.</p>
    </article>
    <article class="project-card">
      <div class="icon-ring"><svg width="34" height="34" viewBox="0 0 24 24" fill="none" stroke="#fff" stroke-width="1.6"><path d="M3 9l9-5 9 5-9 11z"/><path d="M3 9h18"/></svg></div>
      <h3>On the Ground</h3>
      <p>The alliance is hands-on, growing throughout the region. Presently our work focuses on the ground's resilience, watersheds in the Cascades, Willamette and Columbia valleys.</p>
    </article>
    <article class="project-card">
      <div class="icon-ring"><svg width="34" height="34" viewBox="0 0 24 24" fill="none" stroke="#fff" stroke-width="1.6"><path d="M12 21V10"/><path d="M12 10c-4 0-6-3-6-6 4 0 6 3 6 6zM12 13c4 0 6-3 6-6-4 0-6 3-6 6z"/><rect x="4" y="3" width="16" height="18" rx="1"/></svg></div>
      <h3>Ecological Resilience</h3>
      <p>To endure change, communities need healthy watersheds. Our network of professionals brings decades of experience in conservation and restoration.</p>
    </article>
    <article class="project-card">
      <div class="icon-ring"><svg width="34" height="34" viewBox="0 0 24 24" fill="none" stroke="#fff" stroke-width="1.6"><path d="M13 2L5 14h6l-1 8 8-12h-6z"/></svg></div>
      <h3>Energy and Food</h3>
      <p>Security of community food and energy, local and shared, will be an essential part of how communities sustain themselves while minimizing resource demands.</p>
    </article>
  </div>
</section>

<section class="doing">
  <div class="doing-photo" role="img" aria-label="Team working at a desk with laptop and sticky-note whiteboard"></div>
  <div class="doing-panel">
    <h2>What We Are<br>Doing ?</h2>
    <p>We bring partners together across the region to turn adaptation plans into projects on the ground. From restoring floodplains and forests to supporting local food and clean energy, our work connects agencies, districts and landholders with the expertise and funding they need to act now.</p>
  </div>
</section>

<section class="stats" aria-label="Key figures over a dark landscape photo">
  <div><svg width="52" height="52" viewBox="0 0 24 24" fill="none" stroke="#c9a46a" stroke-width="1.3"><circle cx="12" cy="12" r="8"/><path d="M4 12h16M12 4c3 3 3 13 0 16M12 4c-3 3-3 13 0 16"/></svg><div class="stat-num">250+</div><div class="stat-label">Projects Completed</div></div>
  <div><svg width="52" height="52" viewBox="0 0 24 24" fill="none" stroke="#c9a46a" stroke-width="1.3"><path d="M4 14c3 0 5 3 8 3h6M4 14v6M12 4c-2 0-3 2-3 3 0 3 3 5 3 5s3-2 3-5c0-1-1-3-3-3z"/></svg><div class="stat-num">300+</div><div class="stat-label">Donations</div></div>
  <div><svg width="52" height="52" viewBox="0 0 24 24" fill="none" stroke="#c9a46a" stroke-width="1.3"><path d="M7 4h10v5a5 5 0 01-10 0zM12 14v4M8 21h8M7 6H4v2a3 3 0 003 3M17 6h3v2a3 3 0 01-3 3"/></svg><div class="stat-num">17+</div><div class="stat-label">Communities Engaged</div></div>
  <div><svg width="52" height="52" viewBox="0 0 24 24" fill="none" stroke="#c9a46a" stroke-width="1.3"><circle cx="8" cy="8" r="3"/><circle cx="16" cy="8" r="3"/><path d="M2 20c0-4 3-6 6-6s6 2 6 6M10 20c0-4 3-6 6-6s6 2 6 6"/></svg><div class="stat-num">70+</div><div class="stat-label">Volunteers</div></div>
</section>

<section class="themes">
  <div class="theme-card"><div class="theme-photo" role="img" aria-label="Wind turbine at sunset" style="background:linear-gradient(180deg,#f3a43a,#c3652a 60%,#3a2a20)"></div><h4>Energy</h4><span>Investing in clean energy</span></div>
  <div class="theme-card"><div class="theme-photo" role="img" aria-label="Green crop rows in a field" style="background:linear-gradient(180deg,#a9c7e0,#6f9a3c 45%,#3f6a22)"></div><h4>Food Security</h4><span>Rebuilding regional food production</span></div>
  <div class="theme-card"><div class="theme-photo" role="img" aria-label="Eroded riverbank and forest soil" style="background:linear-gradient(160deg,#7a5b3e,#5b4330 50%,#3a3026)"></div><h4>Ecological Resilience</h4><span>Environmental Progress</span></div>
  <div class="theme-card"><div class="theme-photo" role="img" aria-label="Road stretching through a sunlit landscape" style="background:linear-gradient(180deg,#e8c98e,#c9a16a 55%,#6c5a48)"></div><h4>Infrastructure</h4><span>Lasting support</span></div>
</section>

<section class="savings">
  <div class="savings-head"><div class="top">Think Green !</div><div class="big">Save Money</div></div>
  <div class="bars">
    <div class="bar-row"><div class="bar-label">Clean Water</div><div class="bar-track"><div class="bar-fill" style="width:98%;background:linear-gradient(90deg,#f0a02a,#e03a1e)"></div><span class="bar-val">98%</span></div></div>
    <div class="bar-row"><div class="bar-label">Forest Rescue</div><div class="bar-track"><div class="bar-fill" style="width:56%;background:linear-gradient(90deg,#9bd14a,#2ea84a)"></div><span class="bar-val">56%</span></div></div>
    <div class="bar-row"><div class="bar-label">Agriculture</div><div class="bar-track"><div class="bar-fill" style="width:77%;background:linear-gradient(90deg,#6a7be8,#a048d8)"></div><span class="bar-val">77%</span></div></div>
    <div class="bar-row"><div class="bar-label">Alternative Energy</div><div class="bar-track"><div class="bar-fill" style="width:96%;background:linear-gradient(90deg,#3fd6e8,#4aa0e8)"></div><span class="bar-val">96%</span></div></div>
  </div>
</section>

<section class="contact">
  <div class="contact-info">
    <h2>Contact Us</h2>
    <div class="info-line"><svg width="14" height="14" viewBox="0 0 24 24" fill="#8d6a3f"><path d="M12 2a7 7 0 00-7 7c0 5 7 13 7 13s7-8 7-13a7 7 0 00-7-7zm0 10a3 3 0 110-6 3 3 0 010 6z"/></svg><span>1200 Harbor Ave<br>Bellingham WA 98225</span></div>
    <div class="info-line"><svg width="14" height="14" viewBox="0 0 24 24" fill="#8d6a3f"><path d="M3 5h18v14H3zm2 2v.5l7 5 7-5V7z"/></svg><span>info@cedarlinecoalition.org</span></div>
    <div class="info-line"><svg width="14" height="14" viewBox="0 0 24 24" fill="#8d6a3f"><path d="M6 2l4 4-2 3c1 3 4 6 7 7l3-2 4 4-3 4C10 22 2 14 2 5z"/></svg><span>(360) 555-0147<br>(360) 555-0182</span></div>
    <div class="follow">Follow Us</div>
    <div class="social"><i></i><i></i><i></i><i></i></div>
  </div>
  <div class="contact-form">
    <h2>Get In Touch</h2>
    <div class="form-grid">
      <div class="field">Name</div><div class="field">Email</div>
      <div class="field">Phone</div><div class="field">Select</div>
      <div class="field area">Message</div>
    </div>
    <span class="btn">SEND NOW</span>
  </div>
</section>

<footer class="footer">
  <div class="footer-cols">
    <div class="footer-brand">
      <div class="name">Cedarline Coalition</div>
      <div class="tag">Implementing Climate Adaptation</div>
      <div class="footer-social"><i></i><i></i><i></i><i></i></div>
    </div>
    <div class="footer-col"><h5>Quick Links</h5><ul><li>About Us</li><li>Causes</li><li>Testimonial</li><li>Events</li><li>Contact Us</li></ul></div>
    <div class="footer-col"><h5>Contact Us</h5><ul>
      <li><svg width="12" height="12" viewBox="0 0 24 24" fill="#ccc"><path d="M12 2a7 7 0 00-7 7c0 5 7 13 7 13s7-8 7-13a7 7 0 00-7-7z"/></svg>1200 Harbor Ave, Bellingham WA</li>
      <li><svg width="12" height="12" viewBox="0 0 24 24" fill="#ccc"><path d="M6 2l4 4-2 3c1 3 4 6 7 7l3-2 4 4-3 4C10 22 2 14 2 5z"/></svg>(360) 555-0147</li>
      <li><svg width="12" height="12" viewBox="0 0 24 24" fill="#ccc"><path d="M3 5h18v14H3zm2 2v.5l7 5 7-5V7z"/></svg>info@cedarlinecoalition.org</li></ul></div>
    <div class="footer-col"><h5>Location</h5><div class="map" role="img" aria-label="Street map showing the office location"></div></div>
  </div>
  <div class="footer-bar">© 2020 Cedarline Coalition . All Rights Reserved</div>
</footer>

</body>
</html>
```